Software allocation system needs a business card design

We need a business card designed for our software platform - www.plotvane.com.au

At the moment the logo and website is all black and white, we are happy for suggestions on implementing some colour throughout either the logo or business card.

Industry/Entity Type

Software

Font styles to use
Sans Serif

Colors

Designer to choose colors to be used in the design.

```html
<!DOCTYPE html>
<html lang="en">
<head>
<meta charset="utf-8">
<title>Plotvane Business Card</title>
<link href="https://fonts.googleapis.com/css2?family=Lato:wght@400;700&family=Josefin+Sans:wght@300&display=swap" rel="stylesheet">
<style>
  :root {
    --stage: #2a2a2b;
    --card: #161718;
    --card-edge: #202224;
    --teal: #1aa7ad;
    --teal-deep: #12878c;
    --white: #ffffff;
    --swatch-blue: #1d6fd1;
    --swatch-green: #2fc95a;
    --swatch-steel: #1f8fc4;
    --swatch-mint: #1fb868;
  }
  * { box-sizing: border-box; margin: 0; padding: 0; }
  html, body { width: 1200px; height: 1000px; overflow: hidden; }
  body {
    background: radial-gradient(ellipse at 50% 40%, #3a3a3b 0%, var(--stage) 70%);
    font-family: "Lato", Arial, sans-serif;
    position: relative;
  }
  .business-card {
    position: absolute;
    left: 170px; top: 140px;
    width: 860px; height: 540px;
    border-radius: 22px;
    overflow: hidden;
    background: linear-gradient(160deg, var(--card-edge) 0%, var(--card) 60%);
    box-shadow: 0 24px 50px rgba(0,0,0,0.55);
  }
  .brand-block { position: absolute; left: 70px; top: 50px; }
  .brand-name {
    font-family: "Josefin Sans", Arial, sans-serif;
    font-weight: 300;
    font-size: 96px;
    letter-spacing: 6px;
    color: var(--teal);
    line-height: 1;
  }
  .brand-tagline {
    margin-top: 10px;
    font-size: 23px;
    letter-spacing: 1.5px;
    color: var(--white);
  }
  .contact-block { position: absolute; left: 70px; top: 205px; color: var(--white); }
  .person-name { font-weight: 700; font-size: 28px; line-height: 1.2; color: var(--teal); letter-spacing: 0.5px; }
  .person-role { font-size: 20px; line-height: 1.2; margin: 2px 0 0 20px; }
  .contact-list { list-style: none; margin: 14px 0 0 20px; font-size: 21px; line-height: 1.3; }
  .contact-label { color: var(--teal); font-weight: 700; margin-right: 6px; }
  .postal-address { margin: 14px 0 0 30px; font-size: 21px; line-height: 1.25; }
  .card-stripe {
    position: absolute; left: 0; right: 0; bottom: 60px;
    height: 8px; background: var(--white);
  }
  .card-band {
    position: absolute; left: 0; right: 0; bottom: 0;
    height: 52px;
    background: linear-gradient(180deg, var(--teal) 0%, var(--teal-deep) 100%);
  }
  .colour-options { position: absolute; right: 145px; top: 768px; text-align: center; }
  .colour-options-title { color: var(--white); font-size: 26px; letter-spacing: 0.5px; }
  .swatch-row { display: flex; gap: 40px; justify-content: center; margin-top: 40px; }
  .swatch { width: 70px; height: 70px; border-radius: 50%; }
  .swatch--blue { background: var(--swatch-blue); }
  .swatch--green { background: var(--swatch-green); }
  .swatch--steel { background: var(--swatch-steel); }
  .swatch--mint { background: var(--swatch-mint); }
</style>
</head>
<body>
  <section class="business-card">
    <div class="brand-block">
      <div class="brand-name">PLOTVANE</div>
      <div class="brand-tagline">PLANNING &amp; COMPLIANCE FOR HEAVY INDUSTRY</div>
    </div>
    <div class="contact-block">
      <div class="person-name">YOUR NAME</div>
      <div class="person-role">CEO</div>
      <ul class="contact-list">
        <li><span class="contact-label">P:</span>123 456 7890</li>
        <li><span class="contact-label">E:</span>hello@plotvane.com.au</li>
        <li><span class="contact-label">W:</span>www.plotvane.com.au</li>
      </ul>
      <div class="postal-address">P.O. Box 218<br>Ryde Park NSW 1604</div>
    </div>
    <div class="card-stripe"></div>
    <div class="card-band"></div>
  </section>

  <aside class="colour-options">
    <div class="colour-options-title">AVAILABLE IN COLORS:</div>
    <div class="swatch-row">
      <div class="swatch swatch--blue"></div>
      <div class="swatch swatch--green"></div>
      <div class="swatch swatch--steel"></div>
      <div class="swatch swatch--mint"></div>
    </div>
  </aside>
</body>
</html>
```